Creative Business Card for my Sail Boat.. Tide & Time

Going to order PLASTIC business cards for my boat.. she is a sailing vessel catamaran named Tide & Time..

Target Market(s)

to impress other boaters with a unique designed plastic card

Contact Information for Business Card

S/V Tide & Time
Captain Owen Hartley
hartley@owen.example
Mobile/WhatsApp 1-555-318-7062
www.sailtideandtime.example

Requirements
Must have
• Cool colors. logo.. and info in Business Card Details.. Thanks! Utilize clear or cloudy plastic in design. Thanks

```html
<!DOCTYPE html>
<html lang="en">
<head>
<meta charset="utf-8">
<title>Tide &amp; Time — Business Card</title>
<link rel="stylesheet" href="https://fonts.googleapis.com/css2?family=Open+Sans:wght@400;600;700&family=Roboto+Condensed:wght@400;700&family=Arimo:wght@400&display=swap">
<style>
  :root {
    --red-bright: #b62226;
    --red-deep: #6a2b1b;
    --stone: #b5aca3;
    --green: #3a9a45;
    --white: #ffffff;
    --yellow: #fdca0a;
    --brown: #4a2411;
    --page: #ffffff;
  }
  * { margin: 0; padding: 0; box-sizing: border-box; }
  html, body { width: 972px; height: 1200px; overflow: hidden; background: var(--page); }
  .sheet { position: relative; width: 972px; height: 1200px; }

  .card { position: absolute; left: 3px; width: 966px; height: 575px; overflow: hidden; }
  .card--front {
    top: 3px;
    background: radial-gradient(ellipse 75% 95% at 74% 26%, var(--red-bright) 0%, #a02a24 45%, var(--red-deep) 100%);
  }
  .card--back { top: 622px; background: var(--yellow); }

  .holder-name {
    position: absolute; left: 96px; top: 62px;
    font-family: "Open Sans", sans-serif; font-size: 39px; letter-spacing: 0.5px;
    color: var(--white); white-space: nowrap;
  }
  .holder-name .title { color: var(--green); font-weight: 700; }
  .holder-name .first { font-weight: 700; }
  .holder-name .last { font-weight: 400; }

  .icon-band { position: absolute; left: 0; top: 134px; width: 148px; height: 307px; background: var(--stone); }
  .icon-disc {
    position: absolute; left: 74px; width: 48px; height: 48px; border-radius: 50%;
    background: var(--white); box-shadow: 0 3px 4px rgba(0,0,0,0.35);
    display: flex; align-items: center; justify-content: center;
  }
  .icon-disc svg { width: 26px; height: 26px; }

  .contact { position: absolute; left: 173px; font-family: "Roboto Condensed", sans-serif; color: var(--white); font-size: 29px; line-height: 36px; white-space: nowrap; }
  .contact--address { top: 158px; }
  .contact--phone { top: 256px; }
  .contact--email { top: 309px; }
  .contact--web { top: 364px; font-size: 27px; }
  .rule-green { position: absolute; left: 174px; top: 241px; width: 76px; height: 4px; background: var(--green); }
  .divider { position: absolute; left: 532px; top: 134px; width: 3px; height: 307px; background: var(--stone); }

  .brand-name {
    position: absolute; font-family: "Roboto Condensed", sans-serif; font-weight: 700;
    text-align: center; white-space: nowrap;
  }
  .card--front .brand-name { left: 585px; width: 320px; top: 190px; font-size: 64px; color: var(--white); }
  .card--back .brand-name { left: 333px; width: 300px; top: 200px; font-size: 64px; color: var(--brown); }

  .follow-label { position: absolute; font-family: "Arimo", sans-serif; font-size: 19px; color: var(--brown); letter-spacing: 0.5px; text-align: center; }
  .card--front .follow-label { left: 662px; top: 332px; width: 167px; height: 28px; line-height: 28px; background: var(--yellow); border-radius: 5px; }
  .card--back .follow-label { left: 386px; top: 330px; width: 200px; }

  .social-row { position: absolute; display: flex; gap: 10px; }
  .card--front .social-row { left: 662px; top: 375px; }
  .card--back .social-row { left: 402px; top: 372px; }
  .social-box { width: 49px; height: 49px; border-radius: 8px; border: 2px solid var(--white); }
  .card--back .social-box { border-color: var(--brown); }

  .back-web { position: absolute; left: 0; width: 966px; top: 480px; text-align: center; font-family: "Roboto Condensed", sans-serif; font-size: 31px; color: var(--brown); }
</style>
</head>
<body>
<div class="sheet">

  <section class="card card--front">
    <h1 class="holder-name"><span class="title">CAPTAIN</span> <span class="first">OWEN</span> <span class="last">HARTLEY</span></h1>

    <div class="icon-band"></div>
    <div class="icon-disc" style="top:157px">
      <svg viewBox="0 0 24 24"><path d="M12 2a7 7 0 0 0-7 7c0 5 7 13 7 13s7-8 7-13a7 7 0 0 0-7-7zm0 9.5A2.5 2.5 0 1 1 12 6.5a2.5 2.5 0 0 1 0 5z" fill="var(--brown)"/></svg>
    </div>
    <div class="icon-disc" style="top:247px">
      <svg viewBox="0 0 24 24"><path d="M6.6 10.8a15 15 0 0 0 6.6 6.6l2.2-2.2a1 1 0 0 1 1-.25 11.4 11.4 0 0 0 3.6.57 1 1 0 0 1 1 1V20a1 1 0 0 1-1 1A17 17 0 0 1 3 4a1 1 0 0 1 1-1h3.5a1 1 0 0 1 1 1c0 1.25.2 2.45.57 3.57a1 1 0 0 1-.25 1z" fill="var(--brown)"/></svg>
    </div>
    <div class="icon-disc" style="top:302px">
      <svg viewBox="0 0 24 24"><rect x="2.5" y="5" width="19" height="14" fill="none" stroke="var(--brown)" stroke-width="2"/><path d="M2.5 5l9.5 8 9.5-8M2.5 19l7-6.5M21.5 19l-7-6.5" fill="none" stroke="var(--brown)" stroke-width="1.8"/></svg>
    </div>
    <div class="icon-disc" style="top:357px">
      <svg viewBox="0 0 24 24" fill="none" stroke="var(--brown)" stroke-width="1.6"><circle cx="12" cy="12" r="9.5"/><ellipse cx="12" cy="12" rx="4.2" ry="9.5"/><path d="M2.5 12h19M4 7h16M4 17h16"/></svg>
    </div>

    <p class="contact contact--address">123 Stree, Your City<br>Country 1234</p>
    <div class="rule-green"></div>
    <p class="contact contact--phone">1-555-318-7062</p>
    <p class="contact contact--email">hartley@owen.example</p>
    <p class="contact contact--web">www.sailtideandtime.example</p>

    <div class="divider"></div>

    <p class="brand-name">Tide &amp; Time</p>
    <p class="follow-label">follow us on:</p>
    <div class="social-row" aria-label="social profiles">
      <span class="social-box"></span><span class="social-box"></span><span class="social-box"></span>
    </div>
  </section>

  <section class="card card--back">
    <p class="brand-name">Tide &amp; Time</p>
    <p class="follow-label">follow us on:</p>
    <div class="social-row" aria-label="social profiles">
      <span class="social-box"></span><span class="social-box"></span><span class="social-box"></span>
    </div>
    <p class="back-web">www.sailtideandtime.example</p>
  </section>

</div>
</body>
</html>
```